Flyer for spiritual retreat (yoga, meditation, reiki, raw food)

I would like a flyer to promote my upcoming retreat and a matching Facebook banner.

The name of the retreat is "Wavecrest Of Calm" and the tagline is "retreat into you"

The activities in the retreat include daily meditation, ecstatic dance, spiritual development workshops on intuition, energy healing etc and a reiki session is included.

I would like a flyer designed to promote this, something that is editable as I will be running this multiple times and will need to adjust the flyer to add the dates etc each time.

edit: add that here will be fully catered raw food and juices, and that the retreat price includes all accomodation, meals and workshops.

Please contact me if you need further info. Please also visit my website www.marithovland.com and www.facebook.com/tolvanahaven to see my current events and promotions.

Thank you,

Marit

Reason: Hi all, thank you all for your submissions. Apologies as I am traveling and do not have much access to internet and will review your submissions and provide feedback as soon as possible. Kind regards, Marit.

Target Market(s)

People who like meditation, yoga, fans of rowan mabry and jasper vinek, those interested in personal and spiritual development.

Industry/Entity Type

Health And Wellness

Requirements
Must have
• Please put the included reiki session as as added bonus. Something like "BONUS 30 minute reiki healing session" in a little star/banner/something that stands out.
• Please emphasise the "light" part of Wavecrest as I am going for a play on words between in the light and enlightenment.
• Please include placeholder text for place, location, time
• Placeholder for price
• My name (see attached file - can change colour to suit) and website (www.marithovland.com)
Nice to have
• I prefer rounded designs, curves rather than block designs.
Should not have
• Tolvana Haven logo

```html
<!DOCTYPE html>
<html lang="en">
<head>
<meta charset="utf-8">
<title>Wavecrest Of Calm – Retreat Flyer</title>
<link href="https://fonts.googleapis.com/css2?family=Great+Vibes&family=Lobster&family=Gelasio&family=Open+Sans:wght@400;600&display=swap" rel="stylesheet">
<style>
  :root {
    --plum: #7d4766;
    --plum-light: #9a6a86;
    --blush-top: #fbf1ef;
    --blush-mid: #f8e1dc;
    --blush-low: #f7eaea;
    --ink: #1e1a1c;
    --charcoal: #3a3a3c;
    --white: #ffffff;
    --glow: #ffe9a8;
  }
  html, body {
    margin: 0;
    width: 1200px;
    height: 1200px;
    overflow: hidden;
    background: var(--white);
  }
  .canvas { position: relative; width: 1200px; height: 1200px; }
  .flyer {
    position: absolute;
    left: 355px; top: 282px;
    width: 490px; height: 635px;
    overflow: hidden;
    background: linear-gradient(180deg, var(--blush-top) 0%, var(--blush-mid) 58%, var(--blush-mid) 76%, var(--blush-low) 100%);
    font-family: "Gelasio", Georgia, serif;
  }
  .hero-art {
    position: absolute; left: 160px; top: 22px;
    width: 260px; height: 282px;
    background: radial-gradient(ellipse 38% 60% at 50% 55%, #7d4766 0%, #8f5a78 35%, rgba(232,190,200,0.7) 60%, rgba(248,225,220,0) 100%);
  }
  .host-name {
    position: absolute; left: 20px; top: 16px;
    font-family: "Great Vibes", cursive;
    font-size: 42px; color: var(--charcoal);
    margin: 0; line-height: 1;
  }
  .host-site {
    position: absolute; left: 24px; top: 66px;
    margin: 0; font-size: 13px; color: var(--plum);
  }
  .bonus-badge {
    position: absolute; left: 341px; top: 27px;
    width: 134px; height: 134px; border-radius: 50%;
    background: radial-gradient(circle at 50% 40%, #6a6a6c 0%, #2e2e30 80%);
    color: var(--white); text-align: center;
  }
  .bonus-badge .bonus-title {
    font-family: "Lobster", cursive;
    font-size: 23px; line-height: 1.15; margin-top: 30px;
  }
  .bonus-badge .bonus-note {
    font-family: "Open Sans", sans-serif; font-size: 10.5px; margin-top: 3px;
  }
  .activity-list {
    position: absolute; left: 16px; top: 124px;
    margin: 0; padding: 0; list-style: none;
    font-size: 17px; line-height: 22.4px; color: var(--plum);
    white-space: nowrap;
  }
  .activity-list .highlight { color: var(--ink); }
  .band-crest {
    position: absolute; left: 195px; width: 100px; height: 34px;
    background: var(--plum);
  }
  .band-crest.upper { top: 292px; border-radius: 50% 50% 0 0 / 100% 100% 0 0; }
  .band-crest.lower { top: 400px; border-radius: 0 0 50% 50% / 0 0 100% 100%; }
  .title-band {
    position: absolute; left: 0; top: 322px; width: 490px; height: 84px;
    background: var(--plum); text-align: center; color: var(--white);
  }
  .title-band::before, .title-band::after {
    content: ""; position: absolute; left: 0; right: 0; height: 1px;
    background: rgba(255,255,255,0.5);
  }
  .title-band::before { top: 4px; }
  .title-band::after { bottom: 4px; }
  .retreat-title {
    font-family: "Lobster", cursive; font-weight: 400;
    font-size: 32px; margin: 14px 0 0; line-height: 1;
    text-shadow: 0 0 6px rgba(255,255,255,0.4);
  }
  .retreat-title .light-word {
    color: var(--glow);
    text-shadow: 0 0 8px rgba(255,240,190,0.95), 0 0 16px rgba(255,230,160,0.7);
  }
  .tagline { font-size: 15px; margin: 3px 0 0 10px; }
  .food-photo {
    position: absolute; left: 14px; top: 455px; width: 276px; height: 89px;
    background: linear-gradient(90deg, #d96a3e 0%, #9cc27a 30%, #e8e2d8 60%, #d7b98a 100%);
    border: 1px solid #c49a6c;
  }
  .price-badge {
    position: absolute; left: 97px; top: 450px;
    width: 100px; height: 100px; border-radius: 50%;
    background: var(--plum); color: var(--white);
    display: flex; align-items: center; justify-content: center;
    font-family: "Open Sans", sans-serif; font-weight: 600; font-size: 32px;
    box-shadow: 0 2px 4px rgba(0,0,0,0.3);
  }
  .yoga-photo {
    position: absolute; left: 269px; top: 394px; width: 208px; height: 172px;
    background: radial-gradient(ellipse 45% 40% at 55% 60%, #2a2a2c 0%, #d98a7c 45%, rgba(247,234,234,0) 80%);
  }
  .event-details { position: absolute; top: 586px; left: 0; width: 490px; }
  .detail { position: absolute; color: var(--plum); font-size: 15px; }
  .detail .rule { display: block; border-bottom: 1.5px dashed var(--plum); margin-top: 12px; }
  .detail.timing { left: 14px; } .detail.timing .rule { width: 99px; }
  .detail.date { left: 150px; } .detail.date .rule { width: 116px; }
  .detail.location { left: 305px; top: 2px; } .detail.location .rule { width: 162px; }
</style>
</head>
<body>
<div class="canvas">
  <article class="flyer">
    <div class="hero-art" role="img" aria-label="Lotus petals behind a seated meditating figure with raised hands"></div>
    <p class="host-name">Marit Hovland</p>
    <p class="host-site">www.marithovland.com</p>

    <div class="bonus-badge">
      <div class="bonus-title">Bonus<br>30 Minute</div>
      <div class="bonus-note">Reiki healing session</div>
    </div>

    <ul class="activity-list">
      <li>Meditaton</li>
      <li>Ecstatic dance</li>
      <li class="highlight">Spiritual development<br>workshops on<br>intuition</li>
      <li>Energy healing</li>
      <li>Reiki session</li>
    </ul>

    <div class="band-crest upper"></div>
    <div class="band-crest lower"></div>
    <header class="title-band">
      <h1 class="retreat-title">Wave<span class="light-word">crest</span> Of Calm</h1>
      <p class="tagline">Retreat into you</p>
    </header>

    <div class="food-photo" role="img" aria-label="Fresh raw salad and cold-pressed juices"></div>
    <div class="price-badge">$ 75</div>
    <div class="yoga-photo" role="img" aria-label="Woman in a seated yoga backbend pose"></div>

    <section class="event-details">
      <div class="detail timing">Timing:<span class="rule"></span></div>
      <div class="detail date">Date:<span class="rule"></span></div>
      <div class="detail location">Location:<span class="rule"></span></div>
    </section>
  </article>
</div>
</body>
</html>
```